Stationery Design
Letterhead, Envelope, Business Card, Email signature design
I need single sided standard sized Business Card [3.5" x 2"]
Myriad Pro
Professional
Corisse Pallant
Brand Manager
4127 Dunford Avenue
Burnaby, B.C. V3K 8T2
604-281-7734 ext. 120
corisse@brightfernco.ca
brightfernco.ca
We are a family-owned school photography company in Western Canada. We've just had a new logo and website designed and need some new stationery.
This is the .ai file we would like to use for the stationery design. Please refer to our website, brightfernco.ca, for more information about our brand.

```html
<!DOCTYPE html>
<html lang="en">
<head>
<meta charset="utf-8">
<title>BrightFern Co – Business Card</title>
<link href="https://fonts.googleapis.com/css2?family=Source+Sans+3:ital,wght@0,400;0,600;0,700;1,700&display=swap" rel="stylesheet">
<style>
  :root {
    --teal: #1e96b8;
    --teal-dark: #137a98;
    --ink: #3b4146;
    --muted: #6b7075;
    --grey-light: #e4e6e8;
    --grey-mid: #a9adb1;
    --paper: #ffffff;
    --backdrop: #d9dcdf;
  }
  html, body {
    margin: 0;
    width: 1200px;
    height: 852px;
    overflow: hidden;
    background: var(--backdrop);
    font-family: "Source Sans 3", "Myriad Pro", sans-serif;
  }
  .business-card {
    position: absolute;
    left: 100px;
    top: 140px;
    width: 1000px;
    height: 571px;
    background: var(--paper);
    border-radius: 22px;
    overflow: hidden;
    box-shadow: 0 10px 30px rgba(0,0,0,0.18);
  }
  .card-swoosh {
    position: absolute;
    inset: 0;
    width: 100%;
    height: 100%;
  }
  .brand {
    position: absolute;
    left: 62px;
    top: 66px;
    display: flex;
    align-items: center;
    gap: 16px;
  }
  .brand-square {
    width: 44px;
    height: 44px;
    background: var(--teal);
  }
  .brand-name {
    font-size: 48px;
    font-weight: 700;
    color: var(--ink);
    letter-spacing: 0.5px;
  }
  .contact {
    position: absolute;
    left: 62px;
    top: 282px;
    color: var(--ink);
    font-size: 20px;
  }
  .contact-address {
    margin: 0 0 18px;
  }
  .contact-list {
    list-style: none;
    margin: 0;
    padding: 0;
  }
  .contact-list li {
    display: flex;
    align-items: center;
    gap: 14px;
    height: 34px;
  }
  .contact-icon {
    width: 20px;
    height: 20px;
    flex: none;
  }
  .person {
    position: absolute;
    right: 255px;
    top: 292px;
    text-align: right;
  }
  .person-name {
    margin: 0;
    font-size: 28px;
    font-weight: 700;
    font-style: italic;
    color: var(--teal);
  }
  .person-role {
    margin: 2px 0 0;
    font-size: 18px;
    font-weight: 600;
    color: var(--muted);
  }
</style>
</head>
<body>
  <main class="business-card">
    <svg class="card-swoosh" viewBox="0 0 1000 571" preserveAspectRatio="none" aria-hidden="true">
      <defs>
        <linearGradient id="greyFade" x1="0" y1="0" x2="1" y2="1">
          <stop offset="0" stop-color="#f1f2f3"/>
          <stop offset="1" stop-color="#9ea3a8"/>
        </linearGradient>
        <linearGradient id="tealFade" x1="0" y1="0" x2="1" y2="0">
          <stop offset="0" stop-color="#1e96b8"/>
          <stop offset="1" stop-color="#137a98"/>
        </linearGradient>
      </defs>
      <path d="M575 0 C 800 110 890 330 855 571 H 800 C 830 360 760 150 575 0 Z" fill="url(#greyFade)"/>
      <path d="M660 0 H1000 V571 H900 C 930 330 860 110 660 0 Z" fill="url(#tealFade)"/>
    </svg>

    <div class="brand">
      <span class="brand-square"></span>
      <span class="brand-name">BrightFern Co</span>
    </div>

    <section class="contact">
      <p class="contact-address">4127 Dunford Avenue Burnaby, B.C. V3K 8T2</p>
      <ul class="contact-list">
        <li>
          <svg class="contact-icon" viewBox="0 0 20 20"><path d="M5 2 L8 6 L6.5 8 C7.5 10 9.5 12 11.5 13.5 L13.5 12 L17.5 15 L16 18 C9 18 2 11 2 4 Z" fill="var(--teal)"/></svg>
          <span>(T) 1-888-512-3096</span>
        </li>
        <li>
          <svg class="contact-icon" viewBox="0 0 20 20"><path d="M5 2 L8 6 L6.5 8 C7.5 10 9.5 12 11.5 13.5 L13.5 12 L17.5 15 L16 18 C9 18 2 11 2 4 Z" fill="var(--teal)"/></svg>
          <span>604-281-7734 ext. 120</span>
        </li>
        <li>
          <svg class="contact-icon" viewBox="0 0 20 20"><rect x="5" y="1" width="10" height="18" rx="2" fill="var(--teal)"/><rect x="7" y="4" width="6" height="9" fill="#fff"/></svg>
          <span>604-219-4408</span>
        </li>
        <li>
          <svg class="contact-icon" viewBox="0 0 20 20"><rect x="6" y="2" width="8" height="5" fill="var(--teal)"/><rect x="2" y="7" width="16" height="7" rx="1.5" fill="var(--teal)"/><rect x="6" y="12" width="8" height="6" fill="var(--teal-dark)"/></svg>
          <span>604-281-7790</span>
        </li>
        <li>
          <svg class="contact-icon" viewBox="0 0 20 20"><circle cx="10" cy="10" r="9" fill="var(--teal)"/><text x="10" y="14.5" font-size="13" font-weight="700" text-anchor="middle" fill="#fff" font-family="sans-serif">@</text></svg>
          <span>corisse@brightfernco.ca</span>
        </li>
        <li>
          <svg class="contact-icon" viewBox="0 0 20 20"><circle cx="10" cy="10" r="8.5" fill="none" stroke="var(--teal)" stroke-width="2"/><ellipse cx="10" cy="10" rx="3.5" ry="8.5" fill="none" stroke="var(--teal)" stroke-width="1.5"/><line x1="1.5" y1="10" x2="18.5" y2="10" stroke="var(--teal)" stroke-width="1.5"/></svg>
          <span>www.brightfernco.ca</span>
        </li>
      </ul>
    </section>

    <section class="person">
      <h1 class="person-name">Corisse Pallant</h1>
      <p class="person-role">Brand Manager</p>
    </section>
  </main>
</body>
</html>
```